Pricing Sheet for HVAC maintenance plan

I have a pricing sheet for our maintenance plan for my HVAC company. I want to have it put in a more appealing format than just a simple spreadsheet. I need it to be easy to read and yet exciting to look at.

Attached is the form in its word document. We need to have a signature line added as well.

Attached is also the company logo

Target Market(s)

Homeowners, both young and old

Industry/Entity Type

Hvac

Font styles to use
Serif

Colors
fbf289
ec1f27
faa54b
ffffff

Requirements
Must have
• Something that is easy to read.
• Must have logo
• Must have a signature and date line added
• Company colors - attached are some screenshots of what the color scheme might be. You can use this to draw inspiration
• Could be done on a dark background including black, as we paint our trucks black
Should not have
• Too much clutter.

```html
<!DOCTYPE html>
<html lang="en">
<head>
<meta charset="utf-8">
<title>Hearthline Heating &amp; Cooling – Maintenance Plan Pricing</title>
<link rel="stylesheet" href="https://fonts.googleapis.com/css2?family=Libre+Baskerville:wght@700&family=Source+Sans+3:wght@400&display=swap">
<style>
  :root {
    --black: #000000;
    --white: #ffffff;
    --ink: #1a1a1a;
    --field-yellow: #f9ea9a;
    --brand-gold: #f3c65a;
    --footer-orange: #d98c33;
  }
  * { margin: 0; padding: 0; box-sizing: border-box; }
  html, body { width: 927px; height: 1200px; overflow: hidden; background: var(--white); }
  body { font-family: "Source Sans 3", Arial, sans-serif; color: var(--ink); }
  .sheet { position: relative; width: 927px; height: 1200px; overflow: hidden; }

  .masthead { position: absolute; left: 0; top: 0; width: 927px; height: 206px; background: var(--black); color: var(--white); }
  .masthead .credentials { position: absolute; left: 66px; top: 130px; font-size: 13.5px; line-height: 16.5px; }
  .masthead .contact { position: absolute; right: 76px; top: 147px; font-size: 13.5px; line-height: 16.5px; text-align: right; }
  .brand { position: absolute; left: 0; right: 0; top: 40px; display: flex; flex-direction: column; align-items: center; gap: 10px; }
  .brand .mark { width: 22px; height: 22px; border-radius: 50%; background: var(--brand-gold); }
  .brand .name { text-align: center; font-family: "Libre Baskerville", Georgia, serif; font-weight: 700; color: var(--brand-gold); font-size: 30px; line-height: 38px; text-transform: uppercase; letter-spacing: 1px; }

  .client-fields { position: absolute; left: 0; top: 232px; width: 927px; }
  .field { height: 30.3px; display: flex; align-items: center; padding-left: 64px; font-size: 18px; text-transform: uppercase; }
  .field:nth-child(odd) { background: var(--field-yellow); }

  .price-table { position: absolute; left: 0; width: 927px; }
  .price-table .head { height: 34px; background: var(--black); color: var(--white); font-family: "Libre Baskerville", Georgia, serif; font-weight: 700; font-size: 16px; text-transform: uppercase; position: relative; }
  .price-table .head span { position: absolute; top: 50%; transform: translateY(-50%); white-space: nowrap; }
  .price-table .head .title { left: 52px; }
  .price-table .head .assured { left: 500px; transform: translate(-50%, -50%); }
  .price-table .head .preferred { left: 790px; transform: translate(-50%, -50%); }
  .price-table .rows { padding-top: 4px; }
  .row { position: relative; height: 22.7px; font-size: 18px; text-transform: uppercase; }
  .row span { position: absolute; top: 50%; transform: translateY(-50%); white-space: nowrap; }
  .row .item { left: 66px; }
  .row .assured { left: 488px; transform: translate(-50%, -50%); }
  .row .preferred { left: 784px; transform: translate(-50%, -50%); }

  .sign-line { position: absolute; top: 1108px; border-top: 1px solid var(--ink); text-align: center; font-size: 17px; padding-top: 5px; text-transform: uppercase; }
  .sign-line.date { left: 66px; width: 330px; }
  .sign-line.signature { left: 462px; width: 391px; }

  .footer { position: absolute; left: 0; top: 1159px; width: 927px; height: 41px; background: var(--footer-orange); font-size: 13.5px; color: var(--ink); }
  .footer span { position: absolute; top: 50%; transform: translateY(-50%); white-space: nowrap; }
</style>
</head>
<body>
<div class="sheet">
  <header class="masthead">
    <div class="credentials">
      NJ Electrical License #10452<br>
      NJ Home Improvement Business<br>
      Registration #13VH0000000<br>
      NJ HVAC Lic # 508
    </div>
    <div class="brand">
      <div class="mark"></div>
      <div class="name">Hearthline<br>Heating &amp; Cooling</div>
    </div>
    <div class="contact">
      www.HearthlineHVAC.com<br>
      Info@HearthlineHVAC.com<br>
      P.O.Box 412&nbsp;&nbsp;&nbsp; Maple Falls, NJ, 07000
    </div>
  </header>

  <section class="client-fields">
    <div class="field">Name</div>
    <div class="field">Address</div>
    <div class="field">City</div>
    <div class="field">Home Phone</div>
    <div class="field">Cell Phone</div>
    <div class="field">Email Address</div>
    <div class="field">Credit Card Number</div>
    <div class="field">Expiration Date/CCV</div>
  </section>

  <section class="price-table" style="top:494px">
    <div class="head"><span class="title">Combination Packages</span><span class="assured">Assured Plan</span><span class="preferred">Preferred Plan</span></div>
    <div class="rows">
      <div class="row"><span class="item">A/C and Electric Heat</span><span class="assured">26.35</span><span class="preferred">47.45</span></div>
      <div class="row"><span class="item">A/C and Gas Furnace</span><span class="assured">26.35</span><span class="preferred">47.45</span></div>
      <div class="row"><span class="item">A/C and Boiler</span><span class="assured">35.00</span><span class="preferred">56.42</span></div>
      <div class="row"><span class="item">Heat Pump</span><span class="assured">31.00</span><span class="preferred">60.42</span></div>
      <div class="row"><span class="item">A/C and Oil Boiler</span><span class="assured">33.00</span><span class="preferred">65.42</span></div>
    </div>
  </section>

  <section class="price-table" style="top:649px">
    <div class="head"><span class="title" style="left:50px">Combination Packages</span><span class="assured">Assured Plan</span><span class="preferred">Preferred Plan</span></div>
    <div class="rows" style="padding-top:6px">
      <div class="row"><span class="item" style="left:63px">A/C Only</span><span class="assured">16.50</span><span class="preferred">31.32</span></div>
      <div class="row"><span class="item" style="left:63px">Gas Furnace Only</span><span class="assured">14.50</span><span class="preferred">24.12</span></div>
      <div class="row"><span class="item" style="left:63px">Gas Boiler Only</span><span class="assured">14.54</span><span class="preferred">35.33</span></div>
      <div class="row"><span class="item" style="left:63px">Oil Boiler</span><span class="assured">16.54</span><span class="preferred">39.33</span></div>
    </div>
  </section>

  <section class="price-table" style="top:780px">
    <div class="head"><span class="title" style="left:50px">Optional Equipment</span><span class="assured">Assured Plan</span><span class="preferred">Preferred Plan</span></div>
    <div class="rows" style="padding-top:3px">
      <div class="row"><span class="item" style="left:68px">Humidifier</span><span class="assured">6.50</span><span class="preferred">9.21</span></div>
      <div class="row"><span class="item" style="left:68px">Electronic Air Cleaner</span><span class="assured">5.00</span><span class="preferred">9.53</span></div>
      <div class="row"><span class="item" style="left:68px">Media Air Cleaner</span><span class="assured">5.65</span><span class="preferred">12.50</span></div>
      <div class="row"><span class="item" style="left:68px">Attic Ventilation Fan</span><span class="assured">9.54</span><span class="preferred">12.45</span></div>
      <div class="row"><span class="item" style="left:68px">Dehumidifier</span><span class="assured">7.12</span><span class="preferred">12.09</span></div>
    </div>
  </section>

  <section class="price-table" style="top:935px">
    <div class="head"><span class="title" style="left:79px">Electric Plan</span><span class="assured">Assured Plan</span><span class="preferred">Preferred Plan</span></div>
    <div class="rows" style="padding-top:3px">
      <div class="row"><span class="item" style="left:65px">Interior Electric</span><span class="preferred">15.23</span></div>
      <div class="row"><span class="item" style="left:65px">Generator Maintenance Plan</span><span class="preferred">34.12</span></div>
      <div class="row"><span class="item" style="left:65px">Prices are per month, per system</span></div>
    </div>
  </section>

  <div class="sign-line date">Date</div>
  <div class="sign-line signature">Client Signature</div>

  <footer class="footer">
    <span style="left:78px">NJ Electrical License #10452</span>
    <span style="left:335px">NJ HVAC Lic # 508</span>
    <span style="left:488px">NJ Home Improvement Business&nbsp; Registration #13VH0000000</span>
  </footer>
</div>
</body>
</html>
```